Coffee Package Design

We need a new package design for a coffee company. Need to be a mix between modern and classic design combined together. We are open to different ideas.
We changing our product name from Café Verlona to Café Rostelli. The picture upload
shows what the product looks like. We want something completely different. The name of the company should go on the back of the package.
Updates

Hello Everyone,

Please read description, we are going with a new name and design for the product.

Café Rostelli. Café Verlona is what we are replacing with Café Rostelli, we are looking for new

look and design, please submit new designs.

There is a change in the description. Please take out Premium coffee blend and replace with Italian Roast.                                    

Industry/Entity Type

Cafe

Requirements
Must have
• You can use up to 6 colors.
Please put these items on design: Café Rostelli (this is the product name), Regular Premium Blend Coffee, 100% Arabica,
Dumbrell & Sons (name of the company), Tyler, TX on the back of the package

The file uploaded is an example of one of our products and how the package film
is sized.

```html
<!DOCTYPE html>
<html lang="en">
<head>
<meta charset="utf-8">
<title>Café Rostelli — Italian Roast Package</title>
<link href="https://fonts.googleapis.com/css2?family=Handlee&family=Tinos&family=Roboto+Condensed:wght@700&display=swap" rel="stylesheet">
<style>
  :root {
    --canvas-bg: #ffffff;
    --pack-black: #0b0b0b;
    --roast-green: #1f7a3c;
    --roast-green-dark: #0f3f1f;
    --flag-green: #129246;
    --flag-white: #f4f4f4;
    --flag-red: #cf2a2a;
    --ink-white: #f2f2f2;
    --street-light: #d9d9d9;
    --street-mid: #8c8c8c;
    --street-dark: #3a3a3a;
  }
  * { box-sizing: border-box; margin: 0; padding: 0; }
  html, body {
    width: 739px; height: 1200px; overflow: hidden;
    background: var(--canvas-bg);
  }
  .package {
    position: absolute; left: 79px; top: 20px;
    width: 580px; height: 1160px;
    overflow: hidden;
    background: var(--pack-black);
  }
  .flag {
    position: absolute; left: 50%; transform: translateX(-50%);
    width: 90px; height: 30px; display: flex;
  }
  .flag span { flex: 1; }
  .flag .green { background: var(--flag-green); }
  .flag .white { background: var(--flag-white); }
  .flag .red { background: var(--flag-red); }
  .flag--top { top: 0; }
  .flag--bottom { bottom: 0; height: 44px; }

  .brand-mark {
    position: absolute; left: 50%; top: 140px; transform: translateX(-50%);
    width: 120px; height: 120px;
    border: 5px solid var(--ink-white); border-radius: 50%;
  }
  .brand-name {
    position: absolute; left: 0; right: 0; top: 380px;
    text-align: center;
    font-family: "Handlee", cursive;
    font-size: 64px; letter-spacing: 2px;
    color: var(--ink-white);
  }
  .roast-band {
    position: absolute; left: 0; right: 0; top: 563px; height: 102px;
    background: var(--roast-green);
    border-top: 4px solid var(--roast-green-dark);
    display: flex; align-items: center; justify-content: center;
  }
  .roast-band__label {
    font-family: "Tinos", serif;
    font-size: 56px; letter-spacing: 3px;
    color: var(--pack-black);
    padding-top: 6px;
  }
  .street-scene {
    position: absolute; left: 0; right: 0; top: 665px; bottom: 0;
    background: linear-gradient(180deg, var(--street-mid) 0%, var(--street-light) 35%, var(--street-mid) 65%, var(--street-dark) 100%);
  }
  .arabica-badge {
    position: absolute; left: 258px; top: 728px;
    width: 116px; height: 116px;
  }
</style>
</head>
<body>
  <main class="package">
    <div class="flag flag--top"><span class="green"></span><span class="white"></span><span class="red"></span></div>

    <div class="brand-mark"></div>
    <h1 class="brand-name">Café Rostelli</h1>

    <div class="roast-band"><p class="roast-band__label">italian roast</p></div>

    <div class="street-scene" role="img" aria-label="Black and white photograph of an Italian street café with awnings, outdoor tables and old buildings"></div>

    <svg class="arabica-badge" viewBox="0 0 116 116" aria-label="100% Arabica, roast strength 4">
      <defs>
        <path id="badge-top" d="M22,58 A36,36 0 0 1 94,58"/>
        <path id="badge-bottom" d="M18,60 A40,40 0 0 0 98,60"/>
      </defs>
      <circle cx="58" cy="58" r="55" fill="#ffffff"/>
      <circle cx="58" cy="58" r="50" fill="none" stroke="#111" stroke-width="3"/>
      <circle cx="58" cy="58" r="18" fill="none" stroke="#111" stroke-width="3"/>
      <text font-family="Roboto Condensed, sans-serif" font-weight="700" font-size="12" fill="#111" letter-spacing="1">
        <textPath href="#badge-top" startOffset="50%" text-anchor="middle">100% ARABICA</textPath>
      </text>
      <text font-family="Roboto Condensed, sans-serif" font-weight="700" font-size="9" fill="#111" letter-spacing="1">
        <textPath href="#badge-bottom" startOffset="50%" text-anchor="middle">ROAST STRENGTH</textPath>
      </text>
      <text x="58" y="66" text-anchor="middle" font-family="Roboto Condensed, sans-serif" font-weight="700" font-size="24" fill="#111">4</text>
    </svg>

    <div class="flag flag--bottom"><span class="green"></span><span class="white"></span><span class="red"></span></div>
  </main>
</body>
</html>
```